Business Card Design

We would like a colorful, engaging, welcoming business card, utilizing our picture of a local lighthouse. We are a Church. We would like the design to mostly feature the colour blue.
Thank you so much to all Designers who sent in submissions to us - it was really hard to make a decision, they were all of such high quality. We would not hesitate to recommend Sketch Harbor to other churches/ businesses.
Kestrel Beacon Fellowship
Industry/Entity Type
Business
Contact Information for Business Card
Kestrel Beacon Fellowship Inc, 17 Merrow Rd, TALLOWVALE WA 6412, Ph: (08) 9517 4063, E: beaconfellowship@quorvex.example, Chatterly logo - Kestrel Beacon Fellowship Inc, Sunday Service 10am, "For God sent not his Son into the world to condemn the world; but that the world through Him might be saved." John 3:17.

```html
<!DOCTYPE html>
<html lang="en">
<head>
<meta charset="utf-8">
<title>Kestrel Beacon Fellowship Inc – Business Card</title>
<link rel="stylesheet" href="https://fonts.googleapis.com/css2?family=Mulish:wght@300;400;600;700;800&display=swap">
<style>
  :root {
    --stage: #333333;
    --sky-blue: #4aaee0;
    --deep-blue: #3a57a0;
    --card-white: #ffffff;
    --card-foot: #5aaedd;
    --photo-top: #1f3f9a;
    --photo-mid: #4a78c8;
    --photo-low: #5d6a4a;
    --verse-white: #ffffff;
  }
  * { margin: 0; padding: 0; box-sizing: border-box; }
  html, body { width: 1200px; height: 1000px; overflow: hidden; }
  body { background: var(--stage); font-family: "Mulish", sans-serif; position: relative; }

  .business-card {
    position: absolute; left: 67px; top: 168px;
    width: 1072px; height: 650px; overflow: hidden;
    background: linear-gradient(to bottom, var(--card-white) 0%, var(--card-white) 50%, #d6e9f6 70%, var(--card-foot) 100%);
  }
  .card-art { position: absolute; inset: 0; }

  .org-name { position: absolute; left: 60px; top: 66px; line-height: 1; }
  .org-name__first { display: block; font-size: 84px; font-weight: 800; color: var(--sky-blue); letter-spacing: -3px; }
  .org-name__second { display: block; font-size: 92px; font-weight: 800; color: var(--deep-blue); letter-spacing: -3px; margin-top: -8px; }
  .org-name__suffix { display: block; font-size: 56px; font-weight: 300; color: var(--sky-blue); letter-spacing: -1px; margin-top: 6px; }

  .contact { position: absolute; left: 61px; top: 334px; list-style: none; color: var(--deep-blue); font-size: 30px; line-height: 41px; }
  .contact__phone { display: flex; align-items: center; gap: 2px; }
  .contact__phone svg { width: 28px; height: 28px; }
  .contact__service { font-weight: 700; }

  .social { position: absolute; left: 778px; top: 446px; display: flex; align-items: center; gap: 12px; color: var(--deep-blue); font-weight: 700; }
  .social__square { width: 59px; height: 59px; background: var(--deep-blue); border-radius: 3px; }
  .social__lead { display: block; font-size: 20px; line-height: 1; }
  .social__name { display: block; font-size: 32px; line-height: 1.1; }

  .verse { position: absolute; left: 61px; top: 534px; width: 960px; color: var(--verse-white); font-size: 30px; font-weight: 400; line-height: 34px; }
  .verse__ref { color: var(--deep-blue); font-weight: 700; font-style: italic; }
</style>
</head>
<body>
  <section class="business-card">
    <svg class="card-art" viewBox="0 0 1072 650" width="1072" height="650">
      <defs>
        <filter id="soft-glow" x="-20%" y="-20%" width="140%" height="140%">
          <feGaussianBlur stdDeviation="22"/>
        </filter>
        <linearGradient id="photo-tones" x1="0" y1="0" x2="0" y2="1">
          <stop offset="0" stop-color="var(--photo-top)"/>
          <stop offset="0.35" stop-color="var(--photo-mid)"/>
          <stop offset="0.6" stop-color="#6a7462"/>
          <stop offset="1" stop-color="var(--photo-low)"/>
        </linearGradient>
      </defs>
      <path class="halo-arc" d="M470 -20 C 480 250, 790 450, 1090 440 L1090 -20 Z" fill="var(--sky-blue)" filter="url(#soft-glow)"/>
      <path class="halo-arc-core" d="M560 0 C 580 230, 820 420, 1072 412 L1072 0 Z" fill="var(--sky-blue)" opacity="0.9"/>
      <path class="lighthouse-photo" role="img" aria-label="Photo of a local lighthouse on a heath-covered hill under a deep blue sky with light beams"
            d="M640 0 C 660 210, 860 380, 1072 392 L1072 0 Z" fill="url(#photo-tones)"/>
    </svg>

    <h1 class="org-name">
      <span class="org-name__first">Kestrel</span>
      <span class="org-name__second">Beacon</span>
      <span class="org-name__suffix">Fellowship Inc.</span>
    </h1>

    <ul class="contact">
      <li class="contact__address">17 Merrow Rd, TALLOWVALE WA 6412</li>
      <li class="contact__phone">
        <svg viewBox="0 0 24 24" aria-hidden="true"><circle cx="12" cy="12" r="10.5" fill="none" stroke="currentColor" stroke-width="1.4"/><path d="M9 6.5c-1.6.6-2.3 2.4-1.6 4.6.9 2.9 3 5.6 5.2 6.7 1.6.8 3 .5 3.6-.4l-1.9-2c-.5.3-1 .4-1.5 0-1.2-.9-2.3-2.7-2.6-4.2-.1-.6.2-1 .7-1.2Z" fill="currentColor"/></svg>
        <span>(08) 9517 4063</span>
      </li>
      <li class="contact__email">e:beaconfellowship@quorvex.example</li>
      <li class="contact__service">Sunday Service 10am</li>
    </ul>

    <div class="social">
      <span class="social__square" aria-hidden="true"></span>
      <span><span class="social__lead">Find us on</span><span class="social__name">Chatterly</span></span>
    </div>

    <p class="verse">For God set not his Son into the world to condemn the world; but that the world through him might be saved. <span class="verse__ref">John 3:17</span></p>
  </section>
</body>
</html>
```